Business Card Design Project

I want a cleaner business card and envelope then what we have now, its too crowded.
Updates

I update with logo, this can be changed anyway you feel it looks best. I also have put gaurantee on there and extended time, this is my first time doing this. Also gave an example of current card

Target Market(s)

a wide array of customers from lattice 700 to small companies and cleints

Industry/Entity Type

Business

Requirements
Must have
• Need to have address, telephone number email
Nice to have
• a sharp professional card that stands out but is still very clean.
Should not have
• Not crazy looking

```html
<!DOCTYPE html>
<html lang="en">
<head>
<meta charset="utf-8">
<title>Halvern Insurance Group – Business Card</title>
<link href="https://fonts.googleapis.com/css2?family=Quicksand:wght@400;500&display=swap" rel="stylesheet">
<style>
  :root {
    --page-bg: #e4e4e4;
    --card-bg: #fbfbfb;
    --card-edge: #d9d9d9;
    --ink: #2f2f2f;
    --ink-soft: #555555;
    --mark: #8a8a8a;
  }
  * { box-sizing: border-box; margin: 0; padding: 0; }
  html, body {
    width: 1075px;
    height: 1200px;
    overflow: hidden;
    background: var(--page-bg);
    font-family: "Quicksand", sans-serif;
    color: var(--ink);
  }
  .sheet {
    width: 1075px;
    height: 1200px;
    display: flex;
    flex-direction: column;
    align-items: center;
    justify-content: center;
    gap: 70px;
  }
  .card {
    width: 770px;
    height: 440px;
    background: var(--card-bg);
    border: 1px solid var(--card-edge);
    box-shadow: 0 6px 18px rgba(0,0,0,0.12);
    display: flex;
    flex-direction: column;
    align-items: center;
    text-align: center;
  }
  .brand {
    display: flex;
    align-items: center;
    gap: 12px;
  }
  .brand-square {
    width: 40px;
    height: 40px;
    background: var(--mark);
  }
  .brand-name {
    font-weight: 500;
    font-size: 20px;
    letter-spacing: 3px;
    color: var(--ink);
    text-transform: uppercase;
  }

  /* back of card */
  .card-back { justify-content: center; }
  .card-back .brand-square { width: 62px; height: 62px; }
  .website {
    margin-top: 26px;
    font-size: 17px;
    font-weight: 500;
    color: var(--ink-soft);
  }
  .address {
    margin-top: 54px;
    font-size: 22px;
    line-height: 1.35;
    color: var(--ink);
  }

  /* front of card */
  .card-front { padding-top: 62px; }
  .person-name {
    margin-top: 42px;
    font-size: 38px;
    font-weight: 400;
    letter-spacing: 2px;
    text-transform: uppercase;
  }
  .person-role {
    margin-top: 4px;
    font-size: 24px;
    letter-spacing: 1px;
    color: var(--ink-soft);
  }
  .contact {
    margin-top: 30px;
    font-size: 23px;
    line-height: 1.8;
  }
</style>
</head>
<body>
  <main class="sheet">
    <section class="card card-back" aria-label="Card back">
      <div class="brand">
        <span class="brand-square"></span>
      </div>
      <p class="website">www.halvernagency.com</p>
      <address class="address" style="font-style: normal;">
        18320 Corwin Ave.<br>
        Maple Ridge, MI 48122
      </address>
    </section>

    <section class="card card-front" aria-label="Card front">
      <div class="brand">
        <span class="brand-square"></span>
        <span class="brand-name">Halvern Insurance Group</span>
      </div>
      <h1 class="person-name">Renata Lowe-Harmon</h1>
      <p class="person-role">operations manager</p>
      <div class="contact">
        <p class="email">rlowe-harmon@halvernagency.com</p>
        <p class="phone">555 014 0293</p>
      </div>
    </section>
  </main>
</body>
</html>
```